distributor of aftermarket auto electrical components

I am after business card design for my new company called
Coral Vehicle Supplies (CORAL as the acronym). I will supplying automotive wiring components, basically from battery to headlight. I will be aiming to sell in the 4wd scene and to auto electricians. i am not worried which colours are used though i would like it to be dynamic.
Updates

sorry guys, i have add a mobile and e-mail address that will need to on there as well. Sorry for theĀ inconvenience.

sorry guys i had erred on my spelling with my e-mail. i have now fixed it in the brief

Target Market(s)

4wd industry, custom cars, RV, auto electricians

Industry/Entity Type

Electrical

Requirements
Must have
• Company Name
ABN number: 47 316 208 594
Director: Morris Tandy
M 0438 271 954
E mtandyo@bellwire.com.au

```html
<!DOCTYPE html>
<html lang="en">
<head>
<meta charset="utf-8">
<title>Coral Vehicle Supplies – Business Card</title>
<link rel="stylesheet" href="https://fonts.googleapis.com/css2?family=Open+Sans:wght@400&display=swap">
<style>
  :root {
    --page-bg: #ece7df;
    --card-dark: #1b1b1e;
    --card-mid: #26262a;
    --panel-light: #2b2b2f;
    --arc-edge: #4a4a4f;
    --name-grey: #b9b9bb;
    --text-light: #f2f2f2;
    --card-shadow: rgba(0, 0, 0, 0.35);
  }
  * { margin: 0; padding: 0; box-sizing: border-box; }
  html, body {
    width: 1200px;
    height: 900px;
    overflow: hidden;
    background: var(--page-bg);
    font-family: "Open Sans", Arial, sans-serif;
  }
  .canvas {
    position: relative;
    width: 1200px;
    height: 900px;
  }
  .card {
    position: absolute;
    left: 291px;
    width: 597px;
    height: 365px;
    overflow: hidden;
    box-shadow: 0 3px 6px var(--card-shadow);
  }
  .card-front {
    top: 65px;
    background: linear-gradient(90deg, var(--card-mid) 0%, var(--card-dark) 60%, var(--card-mid) 100%);
  }
  .card-back {
    top: 452px;
    background: linear-gradient(160deg, var(--card-dark) 0%, var(--card-mid) 55%, #303034 100%);
  }
  .front-arc {
    position: absolute;
    inset: 0;
    width: 597px;
    height: 365px;
  }
  .brand {
    position: absolute;
    width: 190px;
    text-align: center;
  }
  .brand-front { left: 33px; top: 138px; }
  .brand-back { left: 193px; top: 138px; }
  .brand-name {
    display: block;
    font-size: 48px;
    line-height: 64px;
    font-weight: 400;
    letter-spacing: 3px;
    color: var(--name-grey);
  }
  .brand-tagline {
    display: block;
    margin-top: 11px;
    font-size: 13px;
    line-height: 18px;
    color: var(--text-light);
  }
  .contact-list {
    position: absolute;
    right: 26px;
    top: 136px;
    list-style: none;
    text-align: right;
  }
  .contact-list li {
    position: relative;
    font-size: 14.5px;
    line-height: 19.7px;
    color: var(--text-light);
    padding-right: 12px;
  }
  .contact-list li::after {
    content: "";
    position: absolute;
    right: 0;
    top: 4px;
    width: 2px;
    height: 13px;
    background: var(--text-light);
  }
</style>
</head>
<body>
<main class="canvas">
  <section class="card card-front" aria-label="Card front">
    <svg class="front-arc" viewBox="0 0 597 365" aria-hidden="true">
      <path d="M0 0 H229 C320 50 345 290 170 365 H0 Z" fill="var(--panel-light)"/>
      <path d="M229 0 C320 50 345 290 170 365" fill="none" stroke="var(--arc-edge)" stroke-width="3"/>
    </svg>
    <div class="brand brand-front">
      <span class="brand-name">CORAL</span>
      <span class="brand-tagline">Coral Vehicle Supplies</span>
    </div>
    <ul class="contact-list">
      <li>ABN number: 47 316 208 594</li>
      <li>Director: Morris Tandy</li>
      <li>M 0438 271 954</li>
      <li>E mtandyo@bellwire.com.au</li>
    </ul>
  </section>

  <section class="card card-back" aria-label="Card back">
    <div class="brand brand-back">
      <span class="brand-name">CORAL</span>
      <span class="brand-tagline">Coral Vehicle Supplies</span>
    </div>
  </section>
</main>
</body>
</html>
```